HomeBridle business card and stationary design

We are looking for a simple yet elegant design for our mortgage company business card and stationary.

The card should include:
Name (Derek Walsh)
Title (CEO)
Phone Number (614-208-3917)
Address (48 Birchfield Court, Suite 314, Marlow, OH 43952)
Email (email@homebridle-example.com)
"NMLS" i.e. (NMLS 61947)
"Company NMLS" (Company NMLS 472815)

See above

```html
<!DOCTYPE html>
<html lang="en">
<head>
<meta charset="utf-8">
<title>HomeBridle Business Card</title>
<link href="https://fonts.googleapis.com/css2?family=Montserrat:wght@400;500;600;700&display=swap" rel="stylesheet">
<style>
  :root {
    --backdrop: #2a2c30;
    --navy: #1b2631;
    --ink: #1c2530;
    --sky: #27a8e0;
    --paper: #ffffff;
    --rule: #1c2530;
  }
  * { box-sizing: border-box; margin: 0; padding: 0; }
  html, body {
    width: 1200px; height: 900px; overflow: hidden;
    background: var(--backdrop);
    font-family: "Montserrat", sans-serif;
  }
  .sheet {
    position: relative; width: 1200px; height: 900px;
    display: flex; flex-direction: column; align-items: center; justify-content: center; gap: 60px;
  }
  .card {
    position: relative; width: 560px; height: 320px; border-radius: 22px;
    box-shadow: 0 10px 30px rgba(0,0,0,.35);
  }
  .card-front { background: var(--navy); display: flex; align-items: center; justify-content: center; }
  .brand-name { font-weight: 600; letter-spacing: .5px; line-height: 1; }
  .card-front .brand-name { color: var(--paper); font-size: 64px; }
  .card-back { background: var(--paper); color: var(--ink); }
  .card-back .brand-name { position: absolute; top: 62px; right: 40px; color: var(--ink); font-size: 34px; }
  .holder { position: absolute; left: 40px; top: 58px; }
  .holder-name { font-size: 26px; font-weight: 700; letter-spacing: 1px; text-transform: uppercase; }
  .holder-name .surname { color: var(--sky); }
  .holder-title { font-size: 13px; font-weight: 500; margin-top: 2px; letter-spacing: .5px; }
  .divider-line { position: absolute; left: 40px; right: 40px; top: 136px; height: 1.5px; background: var(--rule); }
  .contact { position: absolute; left: 40px; top: 154px; font-size: 13px; line-height: 22px; }
  .contact .license { color: var(--sky); font-weight: 600; letter-spacing: .5px; }
  .contact li { list-style: none; display: flex; align-items: center; gap: 8px; }
  .contact svg { width: 12px; height: 12px; fill: var(--sky); flex: none; }
  .column-rule { position: absolute; left: 290px; top: 200px; width: 1.5px; height: 76px; background: var(--rule); }
  .office { position: absolute; left: 308px; top: 204px; font-size: 13px; line-height: 20px; }
  .office .license { color: var(--sky); font-weight: 600; letter-spacing: .5px; }
</style>
</head>
<body>
<main class="sheet">
  <section class="card card-front">
    <span class="brand-name">HomeBridle</span>
  </section>

  <section class="card card-back">
    <div class="holder">
      <p class="holder-name">Derek <span class="surname">Walsh</span></p>
      <p class="holder-title">CEO</p>
    </div>
    <span class="brand-name">HomeBridle</span>
    <div class="divider-line"></div>

    <ul class="contact">
      <li class="license">NMLS 61947</li>
      <li>
        <svg viewBox="0 0 24 24" aria-hidden="true"><path d="M6.6 10.8a15 15 0 0 0 6.6 6.6l2.2-2.2a1 1 0 0 1 1-.25 11.4 11.4 0 0 0 3.6.57 1 1 0 0 1 1 1V20a1 1 0 0 1-1 1A17 17 0 0 1 3 4a1 1 0 0 1 1-1h3.5a1 1 0 0 1 1 1c0 1.25.2 2.45.57 3.57a1 1 0 0 1-.25 1z"/></svg>
        614-208-3917
      </li>
      <li>
        <svg viewBox="0 0 24 24" aria-hidden="true"><path d="M2 5h20v14H2z M2 5l10 8 10-8" /></svg>
        email@homebridle-example.com
      </li>
      <li>
        <svg viewBox="0 0 24 24" aria-hidden="true"><circle cx="12" cy="12" r="10"/></svg>
        www.homebridle.com
      </li>
    </ul>

    <div class="column-rule"></div>
    <div class="office">
      <p class="license">Company NMLS 472815</p>
      <p>48 Birchfield Court, Suite 314</p>
      <p>Marlow, OH 43952</p>
    </div>
  </section>
</main>
</body>
</html>
```